Jewelry Shop Needs a Business Card Design

***We want a very sharp and unforgettable pantone for the Business Card. ***
***We do not want the business card or logo only in black, white and grey color!!!Please provide us a main color as our brand topic! Thanks!! ***

Mabel’s Nook is a Hong Kong based fine jewelry brand.

We want a very nice, simple and elegant business card design for Mabel's Nook Brand. The company's logo has been uploaded already.

You can design with below info:

Dorian Fung
Director
M: +852 94273658
T: +852 35820417
F: +852 35820419
E: dorian.fung@mabelsnook.example
5/F , Harbourlight Tower, 12-18 Orchid Lane, Wan Tung Kok, Kowloon, Hong Kong

Target Market(s)

Mabel’s Nook philosophy is a jewelry icon of young, creative, trendy, fashionable, stylish, energetic, and elegant. For Mabel’s Nook, jewelry is one collection of artworks, the most important items in personal life.

Industry/Entity Type

Jewelry

Requirements
Must have
• We want a very sharp and unforgettable pantone for the Business Card.

```html
<!DOCTYPE html>
<html lang="en">
<head>
<meta charset="utf-8">
<title>Mabel’s Nook — Business Card</title>
<link href="https://fonts.googleapis.com/css2?family=Cinzel:wght@400;500&family=Arimo:wght@400&display=swap" rel="stylesheet">
<style>
  :root {
    --backdrop: #e6e4e0;
    --marigold: #f0a020;
    --marigold-deep: #d98f12;
    --marigold-ring: #c9850f;
    --taupe: #8a8175;
    --ink: #1b1b1b;
    --paper: #ffffff;
    --paper-shade: #ececec;
    --text: #2a2a2a;
  }
  * { box-sizing: border-box; margin: 0; padding: 0; }
  html, body { width: 1200px; height: 1072px; overflow: hidden; }
  body {
    background: var(--backdrop);
    position: relative;
    font-family: "Arimo", Arial, sans-serif;
  }
  .card {
    position: absolute;
    left: 250px;
    width: 700px;
    height: 400px;
    border-radius: 28px;
    overflow: hidden;
    box-shadow: 0 10px 28px rgba(0,0,0,0.25);
  }
  /* Front */
  .card-front { top: 100px; background: var(--marigold); }
  .corner-disc {
    position: absolute;
    width: 140px; height: 140px;
    border-radius: 50%;
    background: var(--marigold-deep);
    border: 2px solid var(--marigold-ring);
  }
  .corner-disc.top-right { right: -20px; top: -30px; }
  .corner-disc.bottom-left { left: -20px; bottom: -30px; }
  .front-name {
    position: absolute; left: 0; right: 0; top: 176px;
    text-align: center;
    font-family: "Cinzel", Georgia, serif;
    font-size: 40px;
    letter-spacing: 3px;
    color: var(--taupe);
  }
  /* Back */
  .card-back {
    top: 572px;
    background: radial-gradient(circle at 55% 40%, var(--paper) 0%, var(--paper) 45%, var(--paper-shade) 100%);
  }
  .brand-disc {
    position: absolute; left: 72px; top: 48px;
    width: 130px; height: 130px; border-radius: 50%;
    background: var(--ink);
  }
  .brand-name {
    position: absolute; left: 48px; top: 196px;
    font-family: "Cinzel", Georgia, serif;
    font-size: 26px; letter-spacing: 1.5px;
    color: var(--ink);
  }
  .holder { position: absolute; right: 44px; top: 70px; text-align: right; }
  .holder-name { font-size: 22px; color: var(--text); }
  .holder-title { font-size: 15px; color: var(--marigold); margin-top: 2px; }
  .divider {
    position: absolute; left: 40px; right: 40px; top: 248px;
    height: 1px;
    background: linear-gradient(90deg, rgba(240,160,32,0.2), var(--marigold) 40%, var(--marigold) 70%, rgba(240,160,32,0.3));
  }
  .contacts { position: absolute; left: 56px; top: 272px; list-style: none; }
  .contacts li {
    display: flex; align-items: center; gap: 12px;
    font-size: 15px; color: var(--text); height: 24px;
  }
  .contacts svg { width: 15px; height: 15px; flex: none; }
  .address {
    position: absolute; right: 44px; top: 276px;
    text-align: right; font-size: 15px; line-height: 22px; color: var(--text);
  }
</style>
</head>
<body>
  <section class="card card-front" aria-label="Card front">
    <div class="corner-disc top-right"></div>
    <div class="corner-disc bottom-left"></div>
    <p class="front-name">Mabel’s Nook</p>
  </section>

  <section class="card card-back" aria-label="Card back">
    <div class="brand-disc"></div>
    <p class="brand-name">Mabel’s Nook</p>

    <div class="holder">
      <p class="holder-name">Dorian Fung</p>
      <p class="holder-title">Director</p>
    </div>

    <div class="divider"></div>

    <ul class="contacts">
      <li>
        <svg viewBox="0 0 16 16"><rect x="2" y="2" width="12" height="12" fill="none" stroke="#f0a020" stroke-width="1.6"/></svg>
        +852 94273658
      </li>
      <li>
        <svg viewBox="0 0 16 16"><rect x="1" y="1" width="14" height="14" rx="2" fill="#f0a020"/><path d="M4 6 q4 -3 8 0 v2 h-2 v-1 h-4 v1 h-2 z M5 9 h6 v3 h-6 z" fill="#fff"/></svg>
        +852 35820417
      </li>
      <li>
        <svg viewBox="0 0 16 16"><rect x="1" y="1" width="14" height="14" rx="2" fill="#f0a020"/><rect x="5" y="3" width="6" height="4" fill="#fff"/><rect x="3" y="7" width="10" height="5" fill="#fff"/><rect x="5" y="9" width="6" height="4" fill="#f0a020"/></svg>
        +852 35820419
      </li>
      <li>
        <svg viewBox="0 0 16 16"><rect x="1" y="1" width="14" height="14" rx="2" fill="#f0a020"/><path d="M4 8 l3 3 l5 -6" fill="none" stroke="#fff" stroke-width="1.8"/></svg>
        dorian.fung@mabelsnook.example
      </li>
    </ul>

    <p class="address">5/F , Harbourlight Tower, 12-18 Orchid Lane<br>Wan Tung Kok, Kowloon, Hong Kong</p>
  </section>
</body>
</html>
```